Tavisco hd highway sign

would like a comercial truck in backround, and would like it very easy to read. Must have company name Tavisco H.D. Mechanical
would like address included 5912 quillby frontage road. would a some bullet points on sign
-Commercial truck and trailer inspection and repair
-Heavy equipment repair
-24/7 Mobile service

```html
<!DOCTYPE html>
<html lang="en">
<head>
<meta charset="utf-8">
<title>Tavisco H.D. Mechanical – Highway Sign</title>
<link href="https://fonts.googleapis.com/css2?family=Poppins:wght@600;800&display=swap" rel="stylesheet">
<style>
  :root {
    --red-deep: #a3000f;
    --red-bright: #e2001c;
    --white: #ffffff;
    --yellow: #fff200;
    --navy: #1b1646;
    --sky-top: #8fb4d6;
    --sky-low: #d7dde3;
    --road: #5b5d62;
  }
  * { margin: 0; padding: 0; box-sizing: border-box; }
  html, body {
    width: 1200px;
    height: 372px;
    overflow: hidden;
    background: var(--white);
  }
  .sign {
    position: relative;
    width: 1200px;
    height: 372px;
    overflow: hidden;
    font-family: "Poppins", sans-serif;
  }
  .sign__backdrop {
    position: absolute;
    inset: 0;
  }
  .sign__title {
    position: absolute;
    left: 34px;
    top: 44px;
    color: var(--white);
    font-weight: 800;
    font-size: 80px;
    line-height: 76px;
    letter-spacing: 0.5px;
    text-transform: uppercase;
  }
  .sign__address {
    position: absolute;
    left: 34px;
    top: 211px;
    width: 476px;
    height: 44px;
    border-radius: 22px;
    background: var(--yellow);
    display: flex;
    align-items: center;
    padding-left: 5px;
    color: var(--navy);
    font-weight: 600;
    font-size: 29px;
  }
  .sign__pin {
    width: 36px;
    height: 36px;
    margin-right: 12px;
    flex: none;
  }
  .sign__services {
    position: absolute;
    left: 36px;
    top: 271px;
    list-style: none;
    color: var(--white);
    font-weight: 600;
    font-size: 16.5px;
    line-height: 27px;
  }
  .sign__services li {
    position: relative;
    padding-left: 22px;
  }
  .sign__services li::before {
    content: "";
    position: absolute;
    left: 0;
    top: 10px;
    width: 7px;
    height: 7px;
    border-radius: 50%;
    background: var(--yellow);
  }
</style>
</head>
<body>
<div class="sign">
  <svg class="sign__backdrop" width="1200" height="372" viewBox="0 0 1200 372" aria-hidden="false">
    <defs>
      <linearGradient id="photoTone" x1="0" y1="0" x2="0" y2="1">
        <stop offset="0" stop-color="var(--sky-top)"/>
        <stop offset="0.55" stop-color="var(--sky-low)"/>
        <stop offset="0.75" stop-color="var(--road)"/>
        <stop offset="1" stop-color="#3f4045"/>
      </linearGradient>
      <linearGradient id="panelRed" x1="0" y1="0" x2="1" y2="0">
        <stop offset="0" stop-color="var(--red-deep)"/>
        <stop offset="0.6" stop-color="var(--red-bright)"/>
      </linearGradient>
    </defs>
    <rect class="sign__photo" x="560" y="0" width="640" height="372" fill="url(#photoTone)" role="img" aria-label="Photo of a red semi truck with a white trailer driving on a highway"/>
    <path class="sign__edge" d="M0 0 H672 C732 120 736 250 652 372 H0 Z" fill="var(--white)"/>
    <path class="sign__panel" d="M0 0 H644 C702 120 706 250 624 372 H0 Z" fill="url(#panelRed)"/>
  </svg>

  <h1 class="sign__title">Tavisco H.D.<br>Mechanical</h1>

  <div class="sign__address">
    <svg class="sign__pin" viewBox="0 0 36 36" aria-hidden="true">
      <circle cx="18" cy="18" r="16" fill="none" stroke="var(--navy)" stroke-width="2.5"/>
      <path d="M18 8 C13.5 8 11 11.2 11 14.8 C11 19.5 18 28 18 28 C18 28 25 19.5 25 14.8 C25 11.2 22.5 8 18 8 Z" fill="var(--navy)"/>
      <circle cx="18" cy="14.8" r="2.6" fill="var(--yellow)"/>
    </svg>
    <span>5912 quillby frontage road</span>
  </div>

  <ul class="sign__services">
    <li>Commercial truck and trailer inspection and repair</li>
    <li>Heavy equipment repair</li>
    <li>24/7 Mobile service</li>
  </ul>
</div>
</body>
</html>
```